Curl Radiant through and through. Hair stylist that specializes in extensions.

I am Marisol I am a hair stylist and I would like a website designed for my hair business.

I currently book clients via my profile on trimnook.example/marisolbrantley

I need a professional website ( curlradiantthroughandthrough.example ) to display photos and prices for services offered.

I would like to have a home page with a brief bio, Image with logo and testimonials at the bottom, and a header with tab that include: menu of services, gallery,and FAQs.

On the "Services" page, I'm not interested in photos on this page. Just the name of the service, brief description, and pricing. I would also like to have, on this page, "Appointment Request" with fields that include: Name, service requested, desired time frame (morning, afternoon, evening), and contact number and email

On the "Gallery" page, I would like pictures only, but arranged and/or presented in a creative way...

Target Market(s)

Women ages 25-55 who interested in hair extension services.

Industry/Entity Type

Hair And Beauty

Coding

Number of Pages Required

5+ page

Font styles to use
Sans Serif

Requirements
Must have
• Must include tabs that include, Menu of services offered, a quick fund link to pay deposits with ease, location, contact information, photo gallery, and policy/faqs.
Nice to have
• If possible i would like to stream music with the ability to be silenced. I would like a neutral color palette tans and beige.
Should not have
• stock images

```html
<!DOCTYPE html>
<html lang="en">
<head>
<meta charset="utf-8">
<title>Curl Radiant through and through</title>
<link rel="stylesheet" href="https://fonts.googleapis.com/css2?family=Open+Sans:wght@400;600;700&display=swap">
<style>
:root{
  --ink:#2b2b2e;
  --text:#555;
  --tan:#c9a883;
  --sand:#e2cfbd;
  --cream:#fdf4ec;
  --band:#cfb08c;
  --footer:#333238;
  --footer-text:#c9c9cc;
  --rule:#46454b;
  --white:#fff;
}
*{box-sizing:border-box;margin:0;padding:0}
html,body{width:715px;height:1200px;overflow:hidden}
body{position:relative;background:var(--white);font-family:"Open Sans",Arial,sans-serif;color:var(--text)}
.abs{position:absolute}

/* header */
.site-header{position:absolute;left:0;top:0;width:715px;height:72px;background:var(--white)}
.brand{left:56px;top:22px;white-space:nowrap}
.brand-name{font-size:18px;font-weight:700;color:var(--ink);letter-spacing:.5px;line-height:1}
.brand-tag{font-size:6.5px;letter-spacing:1.8px;color:var(--ink);margin-top:8px;text-transform:uppercase}
.social-top{left:522px;top:22px;display:flex;gap:9px}
.dot{width:7px;height:7px;border-radius:50%;background:var(--ink)}
.login{left:593px;top:16px;width:63px;height:20px;background:var(--ink);color:var(--white);font-size:7px;font-weight:600;display:flex;align-items:center;justify-content:center}
.main-nav{left:240px;top:53px;display:flex;font-size:7px;font-weight:600;color:var(--ink);text-transform:uppercase;white-space:nowrap}
.main-nav span{padding:0 10px 10px;position:relative}
.main-nav .current{color:var(--tan)}
.main-nav .current::after{content:"";position:absolute;left:0;right:0;bottom:0;height:1.5px;background:var(--tan)}

/* hero */
.hero{position:absolute;left:0;top:72px;width:715px;height:310px;background:var(--sand)}
.slider{left:60px;top:21px;width:270px;height:269px;background:linear-gradient(135deg,#3a2e2b,#6d5445 55%,#2c2a2e)}
.slider-arrow{width:22px;height:22px;border-radius:50%;background:rgba(255,255,255,.55);top:121px}
.slider-arrow svg{display:block}
.fav{left:218px;top:6px;width:34px;height:28px;background:var(--white);border:2px solid #9fd6d0}
.welcome{left:350px;top:21px;width:306px;height:270px;background:var(--white);overflow:hidden}
.welcome h1{position:absolute;left:20px;top:20px;font-size:16px;font-weight:400;color:var(--ink);white-space:nowrap}
.welcome h1 b{font-weight:700}
.portrait{left:16px;top:51px;width:82px;height:90px;background:linear-gradient(160deg,#d9a878,#2a2326 70%)}
.stylist{left:126px;top:55px;width:170px}
.stylist h2{font-size:11.5px;font-weight:400;color:var(--tan);line-height:1.3}
.stylist p{font-size:6.3px;color:var(--ink);text-transform:uppercase;margin-top:2px;line-height:1.35}
.listing{left:126px;top:124px;font-size:11px;font-weight:700;color:var(--ink)}
.bio{left:22px;top:165px;width:264px;font-size:6.4px;line-height:8.6px;color:#666}

/* about */
.section-title{font-size:16px;font-weight:400;color:var(--ink)}
.section-title b{font-weight:700}
.about{position:absolute;left:0;top:382px;width:715px;height:130px;text-align:center}
.about .section-title{margin-top:16px}
.about p{width:580px;margin:11px auto 0;font-size:6.8px;line-height:1.62;color:#666}
.btn-dark{display:inline-block;background:var(--ink);color:var(--white);font-size:7px;font-weight:600;padding:6px 11px;margin-top:13px}

/* gallery */
.gallery{position:absolute;left:60px;top:528px;width:596px;height:160px}
.gallery-nav{right:0;top:7px;display:flex;gap:2px}
.gallery-nav span{width:11px;height:11px;border-radius:50%;border:1px solid var(--ink)}
.gallery-nav span:first-child{border-color:var(--tan)}
.thumbs{top:41px;left:0;display:flex;gap:13px}
.thumb{width:109px;height:109px;border:2px solid #eee}
.t1{background:linear-gradient(135deg,#6b4a36,#2d2524)}
.t2{background:linear-gradient(135deg,#3b302c,#7a6658)}
.t3{background:linear-gradient(135deg,#8e2b2d,#c85a55 55%,#f2dcd3)}
.t4{background:linear-gradient(90deg,#1f1d1f,#3c3537 50%,#1f1d1f)}
.t5{background:linear-gradient(135deg,#3a2a24,#2d3e72)}

/* reviews */
.reviews{position:absolute;left:0;top:726px;width:715px;height:217px;background:var(--cream)}
.reviews .section-title{position:absolute;width:715px;text-align:center;top:22px}
.review{top:64px;width:292px;height:101px;background:var(--white)}
.r1{left:59px}.r2{left:365px}
.avatar{left:17px;top:12px;width:61px;height:61px;border-radius:50%}
.r1 .avatar{background:radial-gradient(circle,#d2a88a,#8fc5d2)}
.r2 .avatar{background:radial-gradient(circle,#c99a78,#e6c067)}
.reviewer{left:17px;top:80px;width:61px;text-align:center;font-size:6px;color:#666;text-transform:uppercase}
.quote{left:107px;top:17px;width:170px;font-size:7.5px;line-height:1.63;color:var(--ink)}

/* cta */
.cta{position:absolute;left:0;top:943px;width:715px;height:49px;background:var(--band)}
.cta p{left:171px;top:17px;font-size:9px;font-weight:600;color:var(--white);letter-spacing:.2px}
.cta .btn{left:443px;top:13px;width:90px;height:22px;background:var(--ink);color:var(--white);font-size:9px;font-weight:600;display:flex;align-items:center;justify-content:center}

/* footer */
.site-footer{position:absolute;left:0;top:992px;width:715px;height:208px;background:var(--footer);color:var(--footer-text)}
.col-title{font-size:7px;color:var(--white);text-transform:uppercase;top:20px}
.hours{left:59px;top:48px;width:136px;font-size:6.5px}
.hours div{display:flex;justify-content:space-between;height:24px;border-bottom:1px solid var(--rule);padding-top:2px}
.hours .more{border:0;justify-content:flex-end;margin-top:6px}
.links{left:257px;top:48px;font-size:7px;line-height:18px}
.contact{left:368px;top:47px;width:136px;font-size:6.5px}
.contact .row{display:flex;gap:9px;border-bottom:1px solid var(--rule);padding:3px 0 10px;margin-bottom:9px}
.contact .row:last-child{border:0;margin-bottom:0}
.contact svg{flex:none}
.social-foot{left:371px;top:143px;display:flex;gap:12px}
.social-foot .dot{background:#9a99a0;width:8px;height:8px}
.map{left:515px;top:46px;width:142px;height:110px;background:linear-gradient(135deg,#efe7d9,#e3d2ad 50%,#f0ebe2)}
.copyright{left:0;top:1181px;width:715px;text-align:center;font-size:6.5px;color:var(--white);font-weight:600}
.copyright span{color:var(--tan)}
.rule{left:60px;top:1167px;width:597px;height:1px;background:var(--rule)}
</style>
</head>
<body>

<header class="site-header">
  <div class="abs brand">
    <div class="brand-name">CURL RADIANT</div>
    <div class="brand-tag">Through &amp; Through</div>
  </div>
  <div class="abs social-top"><span class="dot"></span><span class="dot"></span><span class="dot"></span><span class="dot"></span></div>
  <div class="abs login">LOGIN</div>
  <nav class="abs main-nav">
    <span class="current">Home</span><span>Bio</span><span>Services</span><span>Photo Gallery</span><span>Pay Deposits</span><span>Location</span><span>Contact</span><span>FAQs</span>
  </nav>
</header>

<section class="hero">
  <div class="abs slider" role="img" aria-label="Photo collage of a client with long defined curls">
    <div class="abs slider-arrow" style="left:10px"><svg width="22" height="22"><path d="M13 6l-5 5 5 5" fill="none" stroke="#444" stroke-width="2"/></svg></div>
    <div class="abs slider-arrow" style="left:238px"><svg width="22" height="22"><path d="M9 6l5 5-5 5" fill="none" stroke="#fff" stroke-width="2"/></svg></div>
    <div class="abs fav"><svg width="30" height="24"><path d="M11 18l-6-6a3.5 3.5 0 015-5l1 1 1-1a3.5 3.5 0 015 5z" fill="#444"/><rect x="20" y="6" width="6" height="7" fill="none" stroke="#888" stroke-width=".8"/></svg></div>
  </div>
  <article class="abs welcome">
    <h1>Welcome To <b>CURL RADIANT</b></h1>
    <div class="abs portrait" role="img" aria-label="Portrait of stylist Marisol with signature"></div>
    <div class="abs stylist">
      <h2>Curl Radiant Through &amp; Through by Marisol B.</h2>
      <p>Stylist<br>Curl R.T.T. by Marisol B. @ Keystone Salon Suites</p>
    </div>
    <div class="abs listing">TrimNook</div>
    <p class="abs bio">Creative. Classic. Distinguished. These are just a few attributes that Marisol embodies. received in depth training from Linden School of Hair Design, where I had the opportunity to pair my experience with advanced technical training. My passion for art and design has given me the opportunity to express myself through hair design. I also stay abreast of current trends through industry events, hair shows, and continuing education so that I can offer my clients the best services in hair care, style, and extensions.<br>I've spent the last five years perfecting my method of installing extensions which offers my clients a ... (more)</p>
  </article>
</section>

<section class="about">
  <h2 class="section-title">About <b>Us</b></h2>
  <p>Lorem ipsum dolor sit amet, consectetur adipiscing elit. Sed velit lorem, gravida nec tempor nec, tincidunt sed nibh. Cras pharetra ante suscipit eros varius vehicula. Aenean nisi dolor, suscipit non sagittis vel, faucibus non sem. Donec in quam id ipsum aliquet dapibus. In nec elementum sapien, vel porta velit. Fusce sit amet gravida orci, vitae suscipit nisi. Nam in mollis est. Morbi commodo tellus ac ex volutpat, ac faucibus nisi tincidunt. Integer lacus arcu, scelerisque at feugiat sit amet, consequat eu purus. Morbi rutrum eu arcu sed pellentesque. Praesent lobortis urna a luctus mattis.</p>
  <span class="btn-dark">READ MORE</span>
</section>

<section class="gallery">
  <h2 class="section-title">Our <b>Gallery</b></h2>
  <div class="abs gallery-nav"><span></span><span></span></div>
  <div class="abs thumbs">
    <div class="thumb t1" role="img" aria-label="Soft brown layered waves"></div>
    <div class="thumb t2" role="img" aria-label="Curly extension install"></div>
    <div class="thumb t3" role="img" aria-label="Long red straight hair"></div>
    <div class="thumb t4" role="img" aria-label="Sleek black hair from two angles"></div>
    <div class="thumb t5" role="img" aria-label="Bob cut front and back"></div>
  </div>
</section>

<section class="reviews">
  <h2 class="section-title">Client <b>Reviews</b></h2>
  <article class="abs review r1">
    <div class="abs avatar" role="img" aria-label="Client photo"></div>
    <div class="abs reviewer">Dana R</div>
    <p class="abs quote">I have been looking for a stylist since I moved to Austin for 7 years. I noticed a young ladys hair and she gave me Marisol information. I LOVE MY HAIR. She does an amazing job. Always leave satisfied!!!"</p>
  </article>
  <article class="abs review r2">
    <div class="abs avatar" role="img" aria-label="Client photo"></div>
    <div class="abs reviewer">Kiera M</div>
    <p class="abs quote">"I never leave her shop disappointed! She's miracle worker to say the least :)"</p>
  </article>
</section>

<section class="cta">
  <p class="abs">Ut auctor sed dolor ut imperdiet. Cras lectus mauris.</p>
  <div class="abs btn">Contact Now</div>
</section>

<footer class="site-footer">
  <div class="abs col-title" style="left:60px">Business Hours</div>
  <div class="abs col-title" style="left:257px">Useful Links</div>
  <div class="abs col-title" style="left:368px">Contact Info</div>
  <div class="abs col-title" style="left:513px">Find Us</div>

  <div class="abs hours">
    <div><span>Tuesday</span><span>9:00am&nbsp;&nbsp;&nbsp;&nbsp;—&nbsp;&nbsp;&nbsp;&nbsp;6:00pm</span></div>
    <div><span>Wednesday</span><span>9:00am&nbsp;&nbsp;&nbsp;&nbsp;—&nbsp;&nbsp;&nbsp;&nbsp;6:00pm</span></div>
    <div><span>Thursday</span><span>9:00am&nbsp;&nbsp;&nbsp;&nbsp;—&nbsp;&nbsp;&nbsp;&nbsp;6:00pm</span></div>
    <div class="more"><span>Read More &gt;&gt;</span></div>
  </div>

  <div class="abs links">Home<br>Bio<br>Services<br>Location<br>Contact<br>FAQs</div>

  <div class="abs contact">
    <div class="row"><svg width="8" height="7"><rect x=".5" y=".5" width="7" height="6" fill="none" stroke="#fff"/><path d="M.5 .5l3.5 3 3.5-3" fill="none" stroke="#fff"/></svg><span>name@domain.com</span></div>
    <div class="row"><svg width="8" height="8"><path d="M1 1h2l1 2-1 1a5 5 0 002 2l1-1 2 1v2C4 8 0 4 1 1z" fill="#fff"/></svg><span>555-013-0147</span></div>
    <div class="row"><svg width="8" height="9"><path d="M4 9C1 5 1 4 1 3.5a3 3 0 016 0C7 4 7 5 4 9z" fill="#fff"/><circle cx="4" cy="3.5" r="1" fill="#333238"/></svg><span>4120 Cedar Loop, Suite 8<br>Austin, TX, 78701</span></div>
  </div>
  <div class="abs social-foot"><span class="dot"></span><span class="dot"></span><span class="dot"></span><span class="dot"></span><span class="dot"></span><span class="dot"></span></div>

  <div class="abs map" role="img" aria-label="Street map of the salon location"></div>
</footer>
<div class="abs rule"></div>
<div class="abs copyright">Copyright © 2016 - <span>yoursite</span></div>

</body>
</html>
```